Telecom company needs marketing flyers

We need 3 different flyers to describe our product and how to qualify for the program. This our website to use for the logo and color scheme https://www.brivolinkmobile.com, however do not use the mascot on the flyer.

Attached are examples of a competitors flyers.

```html
<!DOCTYPE html>
<html lang="en">
<head>
<meta charset="utf-8">
<title>Brivolink Mobile – Limited Time Tablet Offer</title>
<link href="https://fonts.googleapis.com/css2?family=Open+Sans:wght@700;800&family=Montserrat:wght@400&family=Roboto+Condensed:wght@300;400&display=swap" rel="stylesheet">
<style>
  :root {
    --brand-blue: #1aa3e8;
    --band-cyan: #05b4d9;
    --cta-blue: #0ea5e9;
    --headline-blue: #0863c4;
    --ink: #1c1c2a;
    --paper: #ffffff;
    --device-dark: #1a1a1a;
  }
  * { margin: 0; padding: 0; box-sizing: border-box; }
  html, body { width: 941px; height: 1200px; overflow: hidden; background: var(--paper); }
  .flyer { position: relative; width: 941px; height: 1200px; background: var(--paper); color: var(--ink); }

  .brand-name {
    position: absolute; left: 77px; top: 52px;
    display: inline-block; text-align: right;
    font-family: "Montserrat", sans-serif; font-weight: 400;
    color: var(--brand-blue); font-size: 44px; letter-spacing: 2px; line-height: 1;
    text-transform: uppercase;
  }
  .brand-name span { display: block; font-size: 20px; letter-spacing: 6px; margin-top: 12px; margin-right: -6px; }

  .limited-band { position: absolute; left: 17px; top: 191px; width: 551px; height: 56px; }
  .limited-band svg { position: absolute; inset: 0; }
  .limited-band p {
    position: absolute; left: 59px; top: 7px;
    font-family: "Open Sans", sans-serif; font-weight: 800;
    font-size: 34px; letter-spacing: 4.4px; color: var(--paper); line-height: 42px;
  }

  .tablet-visual {
    position: absolute; left: 76px; top: 307px; width: 433px; height: 710px;
    border-radius: 34px;
    background:
      linear-gradient(180deg, #eaf4fa 0%, #fbf7fb 35%, #f3d6ea 62%, #d9477a 80%, #3a2a6a 100%) 31px 59px / 371px 592px no-repeat,
      linear-gradient(135deg, #a8a4a2 0%, #3a3837 30%, var(--device-dark) 60%);
    border: 3px solid #555;
  }

  .headline {
    position: absolute; left: 560px; top: 301px;
    font-family: "Open Sans", sans-serif; font-weight: 800;
    font-size: 63px; line-height: 73px; color: var(--headline-blue); letter-spacing: -0.5px;
  }
  .headline .currency { position: relative; top: -24px; font-size: 27px; margin-right: 1px; }

  .offer-note {
    position: absolute; left: 544px; top: 627px;
    font-family: "Montserrat", sans-serif; font-size: 17.5px; color: var(--ink);
  }
  .benefits { position: absolute; left: 544px; top: 671px; width: 304px; list-style: none; }
  .benefits li {
    position: relative; padding-left: 26px; margin-bottom: 12px;
    font-family: "Montserrat", sans-serif; font-size: 17px; line-height: 21px; color: var(--ink);
  }
  .benefits li::before { content: "•"; position: absolute; left: 2px; top: 0; font-size: 15px; }

  .dealer-cta { position: absolute; left: 536px; top: 961px; width: 389px; height: 40px; }
  .dealer-cta svg { position: absolute; inset: 0; }
  .dealer-cta p {
    position: absolute; left: 34px; top: 7px;
    font-family: "Open Sans", sans-serif; font-weight: 700; font-size: 18px; line-height: 24px;
    color: var(--paper); letter-spacing: 0.3px;
  }

  .fine-print {
    position: absolute; left: 85px; top: 1062px; width: 782px;
    font-family: "Roboto Condensed", sans-serif; font-weight: 300;
    font-size: 9.4px; line-height: 12.2px; color: var(--ink);
  }
</style>
</head>
<body>
<main class="flyer">
  <div class="brand-name">Brivolink<span>Mobile</span></div>

  <div class="limited-band">
    <svg width="551" height="56" viewBox="0 0 551 56">
      <polygon points="0,0 551,0 531,56 0,56" fill="var(--band-cyan)"/>
      <g stroke="#ffffff" stroke-opacity="0.55" stroke-width="1">
        <line x1="460" y1="0" x2="420" y2="56"/><line x1="470" y1="0" x2="430" y2="56"/>
        <line x1="480" y1="0" x2="440" y2="56"/><line x1="490" y1="0" x2="450" y2="56"/>
        <line x1="500" y1="0" x2="460" y2="56"/><line x1="510" y1="0" x2="470" y2="56"/>
        <line x1="520" y1="0" x2="480" y2="56"/><line x1="530" y1="0" x2="490" y2="56"/>
        <line x1="540" y1="0" x2="500" y2="56"/><line x1="550" y1="0" x2="510" y2="56"/>
      </g>
    </svg>
    <p>FOR A LIMITED TIME</p>
  </div>

  <div class="tablet-visual" role="img" aria-label="8-inch black tablet showing a sprinter in a brightly lit stadium"></div>

  <h1 class="headline">Get an<br>8" tablet<br>for just<br><span class="currency">$</span>10.01!</h1>

  <p class="offer-note">This special offer won’t last forever!</p>
  <ul class="benefits">
    <li>More data means more email, more video conferencing, more Internet!</li>
    <li>Fast, flexible 5G Network.</li>
    <li>Mobile hotspot included means you can connect other devices to your Brivolink Service.</li>
    <li>Cellular Connectivity lets you take internet anywhere there is coverage.</li>
  </ul>

  <div class="dealer-cta">
    <svg width="389" height="40" viewBox="0 0 389 40">
      <polygon points="15,0 389,0 389,40 0,40" fill="var(--cta-blue)"/>
      <g stroke="#ffffff" stroke-opacity="0.55" stroke-width="1">
        <line x1="330" y1="0" x2="312" y2="40"/><line x1="340" y1="0" x2="322" y2="40"/>
        <line x1="350" y1="0" x2="332" y2="40"/><line x1="360" y1="0" x2="342" y2="40"/>
        <line x1="370" y1="0" x2="352" y2="40"/><line x1="380" y1="0" x2="362" y2="40"/>
        <line x1="389" y1="2" x2="372" y2="40"/>
      </g>
    </svg>
    <p>See your authorized dealer for info!</p>
  </div>

  <p class="fine-print">Promotional offer subject to eligibility for Emergency Broadband Benefit (EBB). The EBB is a temporary FCC program that provides non-transferrable discounts on monthly broadband Internet access service. An eligible household is limited to one monthly service discount. Eligible consumers may get EBB service from Brivolink Mobile or from any participating provider. Benefits may be transferred to another provider at any time. When the FCC announces the end the EBB program or we end our promotional FREE EBB service offer, we will notify you and you will revert to receiving only the standard FREE Lifeline plan if you are eligible, or you may keep your EBB service by paying the applicable undiscounted rate of $40 plus fees and taxes. For more information about EBB eligibility and the program go to brivolinkmobile.com/ebb or call us at 1-800-555-0142.</p>
</main>
</body>
</html>
```